A simple Chatterbook Ad (not Chatterbook Page) for weight loss surgery

It’s a simple ad in terms of the text.

The text should say:
Curious about weight loss surgery?
This 30 second quiz will tell you which procedure will suit you best

I'm open to variations in the text if it is thought to enhance the ad.

Targeted towards obese individuals who have been unable to lose weight with diet and exercise. My industry is weight loss surgery – webpage www.marcusbellweather.com.au. Clicking the ad leads to a quiz on my webpage relating to weight loss surgery. Most frequent users of this service are females (75%) between ages of 35 and 55 years.

Successful weight loss surgery can enable individuals who have been unable to lose weight to lose a substantial amount of the excess weight they are carrying to be healthier and happier.

```html
<!DOCTYPE html>
<html lang="en">
<head>
<meta charset="utf-8">
<title>Weight Loss Surgery – Chatterbook Ad</title>
<link rel="stylesheet" href="https://fonts.googleapis.com/css2?family=Montserrat:wght@400;500;700;800;900&family=Tinos&family=Roboto:wght@400;500;700&display=swap">
<style>
:root{
  --board:#a3a9a9;
  --white:#ffffff;
  --teal:#2fe0d4;
  --teal-mid:#1f8a80;
  --teal-deep:#0c4c46;
  --ink:#050807;
  --ui-text:#1c1e21;
  --ui-grey:#65676b;
  --ui-bar:#f0f2f5;
  --ui-line:#dadde1;
  --skin:#c7936f;
  --shorts:#e9e9ef;
}
*{margin:0;padding:0;box-sizing:border-box}
html,body{width:1200px;height:2351px;overflow:hidden}
body{background:var(--board);position:relative;font-family:"Montserrat",sans-serif}

/* ---------- feed post ---------- */
.post{position:absolute;left:193px;top:179px;width:815px;height:916px;background:var(--white);border-radius:8px 8px 4px 4px;box-shadow:0 10px 0 -2px #6f7373;overflow:hidden;font-family:"Roboto",sans-serif;color:var(--ui-text)}
.post-avatar{position:absolute;left:19px;top:19px;width:48px;height:48px;border-radius:50%;background:#e4e6e6}
.post-avatar::after{content:"";position:absolute;left:14px;top:14px;width:20px;height:20px;border-radius:50%;background:var(--teal-mid)}
.post-name{position:absolute;left:77px;top:21px;font-size:18px;font-weight:700}
.post-meta{position:absolute;left:77px;top:46px;font-size:15px;color:var(--ui-grey)}
.post-more{position:absolute;right:30px;top:26px;font-size:22px;color:var(--ui-grey);letter-spacing:1px}
.post-copy{position:absolute;left:20px;top:78px;width:780px;font-size:17px;line-height:24px}
.post .ad{position:absolute;left:0;top:143px;width:815px;height:569px}
.link-bar{position:absolute;left:0;top:712px;width:815px;height:95px;background:var(--ui-bar)}
.link-url{position:absolute;left:24px;top:12px;font-size:14px;color:var(--ui-grey)}
.link-title{position:absolute;left:24px;top:36px;font-size:19px;font-weight:700}
.link-desc{position:absolute;left:24px;top:64px;font-size:17px;color:var(--ui-grey)}
.link-button{position:absolute;left:670px;top:25px;width:124px;height:43px;border-radius:6px;background:#e4e6eb;font-size:16px;font-weight:500;display:flex;align-items:center;justify-content:center}
.reactions{position:absolute;left:20px;top:807px;width:775px;height:54px;border-bottom:1px solid var(--ui-line);display:flex;align-items:center;font-size:17px;color:var(--ui-grey)}
.react-dot{width:20px;height:20px;border-radius:50%;border:2px solid var(--white)}
.react-like{background:#1877f2}
.react-love{background:#f33e58;margin-left:-4px;margin-right:8px}
.reactions .counts{margin-left:auto}
.actions{position:absolute;left:20px;top:862px;width:775px;height:54px;display:flex;align-items:center;font-size:18px;font-weight:500;color:var(--ui-grey)}
.action{display:flex;align-items:center;gap:8px}
.action svg{width:22px;height:22px;fill:none;stroke:var(--ui-grey);stroke-width:1.8}
.action-like{margin-left:83px}.action-comment{margin-left:150px}.action-share{margin-left:143px}
.viewer{margin-left:auto;margin-right:12px;display:flex;align-items:center;gap:6px}
.viewer i{display:block;width:22px;height:22px;border-radius:50%;background:#5a5060}
.viewer b{width:0;height:0;border:5px solid transparent;border-top:6px solid var(--ui-grey);margin-top:5px}

/* ---------- ad artwork (shared) ---------- */
.ad{overflow:hidden;font-family:"Montserrat",sans-serif;background:linear-gradient(200deg,var(--teal-mid) 0%,var(--teal-deep) 38%,var(--ink) 80%)}
.ad-photo{position:absolute;top:0;right:0;height:100%;background:
  linear-gradient(180deg,var(--white) 0%,var(--skin) 18%,var(--skin) 46%,var(--shorts) 56%,var(--shorts) 100%);
  clip-path:polygon(38% 0,100% 0,100% 100%,28% 100%,22% 55%,30% 30%)}
.ad-header{position:absolute;left:0;top:0;overflow:visible}
.brand{position:absolute;display:flex;align-items:center;font-weight:700;color:var(--teal-mid);letter-spacing:.5px;white-space:nowrap}
.brand-mark{border-radius:50%;background:var(--teal-mid);flex:none}
.eyebrow{position:absolute;color:var(--white);font-weight:500;white-space:nowrap}
.headline{position:absolute;color:var(--white);font-weight:900;line-height:1;white-space:nowrap;letter-spacing:-1px}
.tag{position:absolute;background:var(--teal);color:var(--ink);font-weight:800;display:flex;align-items:center;justify-content:center}
.rule{position:absolute;height:1px;background:rgba(255,255,255,.18)}
.timer{position:absolute}
.quiz{position:absolute;color:var(--white);font-weight:500;white-space:nowrap}
.quiz strong{color:var(--teal);font-weight:800}
.appt{position:absolute;color:var(--white);font-family:"Tinos",serif;white-space:nowrap}
.phone{position:absolute;color:var(--teal);font-weight:900;white-space:nowrap;line-height:1}
.web{position:absolute;color:var(--white);font-family:"Tinos",serif;white-space:nowrap}

/* feed size */
.ad--feed .ad-photo{width:335px}
.ad--feed .brand{left:67px;top:40px;font-size:16px;gap:10px}
.ad--feed .brand-mark{width:30px;height:30px}
.ad--feed .eyebrow{left:68px;top:149px;font-size:18px}
.ad--feed .headline-1{left:66px;top:178px;font-size:47px}
.ad--feed .headline-2{left:66px;top:230px;font-size:47px}
.ad--feed .tag{left:204px;top:238px;width:104px;height:26px;font-size:15px}
.ad--feed .rule-1{left:77px;top:310px;width:265px}
.ad--feed .rule-2{left:77px;top:400px;width:265px}
.ad--feed .timer{left:71px;top:323px;width:58px;height:58px}
.ad--feed .quiz{left:141px;top:324px;font-size:15px;line-height:21px}
.ad--feed .appt{left:77px;top:440px;font-size:18px}
.ad--feed .phone{left:76px;top:467px;font-size:34px}
.ad--feed .web{left:77px;top:501px;font-size:19px}

/* square size */
.ad--square{position:absolute;left:210px;top:1307px;width:813px;height:812px;box-shadow:0 30px 40px rgba(0,0,0,.28)}
.ad--square .ad-photo{width:450px}
.ad--square .brand{left:52px;top:60px;font-size:22px;gap:14px}
.ad--square .brand-mark{width:40px;height:40px}
.ad--square .eyebrow{left:50px;top:227px;font-size:23px}
.ad--square .headline-1{left:49px;top:266px;font-size:60px}
.ad--square .headline-2{left:49px;top:333px;font-size:60px}
.ad--square .tag{left:226px;top:343px;width:134px;height:34px;font-size:20px}
.ad--square .rule-1{left:59px;top:472px;width:351px}
.ad--square .rule-2{left:59px;top:588px;width:351px}
.ad--square .timer{left:56px;top:489px;width:74px;height:74px}
.ad--square .quiz{left:144px;top:489px;font-size:19.5px;line-height:27px}
.ad--square .appt{left:62px;top:638px;font-size:23px}
.ad--square .phone{left:61px;top:674px;font-size:44px}
.ad--square .web{left:62px;top:719px;font-size:25px}
</style>
</head>
<body>

<article class="post">
  <div class="post-avatar"></div>
  <div class="post-name">Marcus Bellweather</div>
  <div class="post-meta">Sponsored · ◍</div>
  <div class="post-more">•••</div>
  <p class="post-copy">Successful weight loss surgery can enable individuals who have been unable to lose weight to lose a substantial amount of the excess weight they are carrying to be healthier and happier.</p>

  <div class="ad ad--feed">
    <div class="ad-photo" role="img" aria-label="Photo of a slim woman in a crop top and white shorts measuring her waist with a yellow tape measure"></div>
    <svg class="ad-header" width="815" height="569" viewBox="0 0 815 569" aria-hidden="true">
      <polygon points="0,98 325,122 366,0 400,0 355,136 0,108" fill="#0b4f48"/>
      <polygon points="0,0 366,0 325,122 0,98" fill="#ffffff"/>
    </svg>
    <div class="brand"><span class="brand-mark"></span>MARCUS BELLWEATHER</div>
    <div class="eyebrow">CURIOUS ABOUT</div>
    <div class="headline headline-1">WEIGHT</div>
    <div class="headline headline-2">LOSS</div>
    <div class="tag">SURGERY?</div>
    <div class="rule rule-1"></div>
    <svg class="timer" viewBox="0 0 74 74" aria-hidden="true">
      <circle cx="37" cy="37" r="33" fill="none" stroke="#ffffff" stroke-width="3" stroke-dasharray="1 3.2"/>
      <text x="37" y="42" text-anchor="middle" font-family="Montserrat,sans-serif" font-weight="800" font-size="24" fill="#fff">30</text>
      <text x="37" y="55" text-anchor="middle" font-family="Montserrat,sans-serif" font-weight="700" font-size="8" fill="#fff">SEC</text>
    </svg>
    <div class="quiz">This <strong>30 second</strong> quiz<br>will tell you which procedure<br>will <strong>suit you best</strong></div>
    <div class="rule rule-2"></div>
    <div class="appt">For all appointments</div>
    <div class="phone">03 9000 4812</div>
    <div class="web">www.marcusbellweather.com.au</div>
  </div>

  <div class="link-bar">
    <div class="link-url">www.marcusbellweather.com.au</div>
    <div class="link-title">Curious about weight loss surgery?</div>
    <div class="link-desc">This 30 second quiz will tell you which procedure will suit you best</div>
    <div class="link-button">Learn more</div>
  </div>
  <div class="reactions">
    <span class="react-dot react-like"></span><span class="react-dot react-love"></span>
    <span>Username, Username and 2K others</span>
    <span class="counts">26 Comments&nbsp;&nbsp;2 Shares</span>
  </div>
  <div class="actions">
    <span class="action action-like"><svg viewBox="0 0 24 24"><path d="M7 10v11H3V10zM7 10l4-7c2 0 3 1 2.5 3L13 10h6a2 2 0 0 1 2 2.3l-1.3 7A2 2 0 0 1 17.7 21H7"/></svg>Like</span>
    <span class="action action-comment"><svg viewBox="0 0 24 24"><path d="M4 4h16v12H9l-5 4z"/></svg>Comment</span>
    <span class="action action-share"><svg viewBox="0 0 24 24"><path d="M14 4l7 7-7 7v-4c-6 0-9 2-11 6 0-7 4-11 11-12z"/></svg>Share</span>
    <span class="viewer"><i></i><b></b></span>
  </div>
</article>

<div class="ad ad--square">
  <div class="ad-photo" role="img" aria-label="Photo of a slim woman in a crop top and white shorts measuring her waist with a yellow tape measure"></div>
  <svg class="ad-header" width="813" height="812" viewBox="0 0 813 812" aria-hidden="true">
    <polygon points="0,135 420,173 477,0 522,0 462,195 0,150" fill="#0b4f48"/>
    <polygon points="0,0 477,0 420,173 0,135" fill="#ffffff"/>
  </svg>
  <div class="brand"><span class="brand-mark"></span>MARCUS BELLWEATHER</div>
  <div class="eyebrow">CURIOUS ABOUT</div>
  <div class="headline headline-1">WEIGHT</div>
  <div class="headline headline-2">LOSS</div>
  <div class="tag">SURGERY?</div>
  <div class="rule rule-1"></div>
  <svg class="timer" viewBox="0 0 74 74" aria-hidden="true">
    <circle cx="37" cy="37" r="33" fill="none" stroke="#ffffff" stroke-width="3" stroke-dasharray="1 3.2"/>
    <text x="37" y="42" text-anchor="middle" font-family="Montserrat,sans-serif" font-weight="800" font-size="24" fill="#fff">30</text>
    <text x="37" y="55" text-anchor="middle" font-family="Montserrat,sans-serif" font-weight="700" font-size="8" fill="#fff">SEC</text>
  </svg>
  <div class="quiz">This <strong>30 second</strong> quiz<br>will tell you which procedure<br>will <strong>suit you best</strong></div>
  <div class="rule rule-2"></div>
  <div class="appt">For all appointments</div>
  <div class="phone">03 9000 4812</div>
  <div class="web">www.marcusbellweather.com.au</div>
</div>

</body>
</html>
```